Etiketten für Brennerei aus Tirol bzw. Südtirol
Zielgruppe
Wir sind eine Brennerei aus Tirol bzw. Südtirol, produzieren in Österreich und beliefern mit unseren Bränden, Schnäpsen und Spirituosen den Lebensmittel Einzelhandel (kein Discount) in Österreich und Deutschland. Zielkunden sind Genießer, die die österreichische bzw. Südtiroler Gastlichkeit und Lebenskultur schätzen.
Aufgabenstellung
Unsere bestehende 1 Liter Edelbrand Linie soll komplett NEU werden, weil schon einige Jahre alt. Referenz:
https://www.karwendo-bergkueche.com/produkte/edelbrände-aus-österreich/
Achtung: nur 1 l Flaschen. Nur Williams Edelbrand als Start. Nur Frontetikett. Alpines Flair - Berge - unser Logo Karwendo Bergküche.
Frucht sehr markant (lackiert beim Druck) - edles Papier als Hintergrund.

```html
<!DOCTYPE html>
<html lang="de">
<head>
<meta charset="utf-8">
<title>Karwendo Bergküche – Williams Edelbrand Etikett</title>
<link rel="stylesheet" href="https://fonts.googleapis.com/css2?family=Pathway+Gothic+One&family=Oswald:wght@300;500&family=Cormorant+Garamond:wght@500&display=swap">
<style>
  :root {
    --paper: #ffffff;
    --stage: #ffffff;
    --green: #a2bb12;
    --grey-text: #6a6a6c;
    --gold-dark: #8c6a14;
    --gold-mid: #b5924a;
    --gold-light: #efe4cc;
    --edge: #c9c9c9;
    --placeholder-top: #e4e4e4;
    --placeholder-bottom: #f7f7f7;
  }
  * { margin: 0; padding: 0; box-sizing: border-box; }
  html, body { width: 1200px; height: 1200px; overflow: hidden; background: var(--stage); }
  .canvas { position: relative; width: 1200px; height: 1200px; }
  .label {
    position: absolute; left: 320px; top: 62px; width: 560px; height: 1096px;
    background: var(--paper); border: 1px solid var(--edge);
  }
  .mountain-art {
    position: absolute; left: 0; top: 0; width: 470px; height: 90px;
    background: linear-gradient(180deg, var(--placeholder-top), var(--placeholder-bottom));
  }
  .accent { position: absolute; right: -1px; width: 88px; background: var(--green); }
  .accent--top { top: 48px; height: 92px; }
  .accent--mid { top: 532px; height: 52px; }
  .accent--bottom { top: 1044px; height: 51px; }
  .variety {
    position: absolute; left: 470px; top: 515px; width: 340px;
    transform: rotate(-90deg); transform-origin: 0 0;
    font-family: "Cormorant Garamond", Georgia, serif; font-weight: 500;
    font-size: 86px; line-height: 1; letter-spacing: 4px;
    color: var(--green); text-align: center; white-space: nowrap;
  }
  .category {
    position: absolute; right: 90px; top: 174px;
    font-family: "Oswald", "Arial Narrow", sans-serif; font-weight: 300;
    font-size: 54px; letter-spacing: 3px; color: var(--grey-text); line-height: 1;
  }
  .premium-tag {
    position: absolute; left: 0; top: 230px; width: 204px; height: 76px;
    background: var(--green); border-radius: 0 14px 0 0;
    transform: skewY(-9deg); transform-origin: 0 100%;
  }
  .premium-tag span {
    position: absolute; left: 10px; top: 14px; transform: skewY(9deg) rotate(-9deg);
    font-family: "Cormorant Garamond", Georgia, serif; font-weight: 500;
    font-size: 44px; color: var(--paper); letter-spacing: 1px; line-height: 1;
  }
  .fruit-photo {
    position: absolute; left: 20px; top: 280px; width: 385px; height: 290px;
    border-radius: 48% 52% 46% 50%;
    background: radial-gradient(ellipse at 50% 45%, #d6cf2c 0%, #c8c22a 45%, #e6c857 70%, rgba(255,255,255,0) 74%);
  }
  .quality {
    position: absolute; right: 20px; top: 632px; text-align: right;
    font-family: "Pathway Gothic One", "Arial Narrow", sans-serif;
    font-size: 40px; line-height: 54px; letter-spacing: 1.5px; color: var(--gold-mid);
  }
  .strength {
    position: absolute; right: 20px; top: 784px;
    font-family: "Pathway Gothic One", "Arial Narrow", sans-serif;
    font-size: 42px; letter-spacing: 1.5px; color: var(--gold-dark); line-height: 1;
  }
  .brand-band {
    position: absolute; left: -1px; top: 884px; width: 560px; height: 160px;
    background: linear-gradient(90deg, var(--gold-dark) 0%, #c6a866 22%, var(--gold-light) 40%, #a88431 58%, var(--gold-light) 80%, var(--gold-dark) 100%);
    display: flex; align-items: center; justify-content: center; gap: 16px;
  }
  .brand-mark { width: 14px; height: 14px; background: var(--paper); }
  .brand-name {
    font-family: "Oswald", "Arial Narrow", sans-serif; font-weight: 500;
    color: var(--paper); text-align: center; line-height: 1.15;
    font-size: 40px; letter-spacing: 4px;
  }
</style>
</head>
<body>
<main class="canvas">
  <article class="label">
    <div class="mountain-art" role="img" aria-label="Line drawing of an alpine mountain range along the top edge"></div>

    <div class="accent accent--top"></div>
    <div class="variety">Williams</div>
    <div class="accent accent--mid"></div>

    <h1 class="category">EDELBRAND</h1>
    <div class="premium-tag"><span>Premium</span></div>
    <div class="fruit-photo" role="img" aria-label="Photograph of three ripe yellow Williams pears with water droplets"></div>

    <p class="quality">Beste Qualität<br>Optima Qualitata</p>
    <p class="strength">40% vol</p>

    <div class="brand-band">
      <span class="brand-mark"></span>
      <span class="brand-name">KARWENDO<br>BERGKÜCHE</span>
    </div>
    <div class="accent accent--bottom"></div>
  </article>
</main>
</body>
</html>
```